Webdesign für visa-korvenet.org
Kreativer Initialvorschlag, schnelle Umsetzung, flexible Anpassung des Designvorschlags und nette Kommunikation, gerne wieder!
Zielgruppe
Wir vermitteln weltweit Reisegenehmigungen für Geschäfts- und Privatkunden. Auf VISA-Korvenet.org möchten wir auf deutsch, englisch & chinesisch Reisenden bei der Beiholung von Kurzzeit, Work & Travel & diversen Visaarten helfen.
Aufgabenstellung
Der Webseitezweck ist es, dass Besucher bestellen. Dafür muss die Seite attraktiv, einfach bedienbar und das CTA Element "zum Formular" präsent und mehrfach auftauchen.

```html
<!DOCTYPE html>
<html lang="de">
<head>
<meta charset="utf-8">
<title>Visa Korvenet – Evisitor Visum Australien</title>
<link rel="stylesheet" href="https://fonts.googleapis.com/css2?family=Montserrat:wght@300;400;500;700&display=swap">
<style>
:root{
  --navy:#022a7c;
  --navy-deep:#0b1f5c;
  --red:#c8103a;
  --text:#333;
  --muted:#555;
  --white:#fff;
  --footer:#d9d9d9;
}
*{box-sizing:border-box;margin:0;padding:0}
html,body{width:1200px;height:2521px;overflow:hidden}
body{font-family:'Montserrat',sans-serif;font-weight:300;color:var(--text);background:var(--white);position:relative}
a{color:inherit;text-decoration:none}

.site-header{position:absolute;top:0;left:0;width:1200px;height:64px;background:var(--navy);color:var(--white)}
.brand{position:absolute;left:38px;top:14px;display:flex;align-items:center;gap:10px;font-size:20px;font-weight:400}
.brand-dot{width:34px;height:34px;border-radius:50%;background:var(--red)}
.main-nav{position:absolute;left:305px;top:0;display:flex;height:64px}
.main-nav a{width:110px;display:flex;flex-direction:column;align-items:center;justify-content:center;gap:6px;font-size:10.5px;font-weight:400}
.main-nav svg{width:15px;height:15px;fill:var(--white)}
.nav-cta{position:absolute;right:38px;top:0;width:165px;height:64px;background:var(--red);display:flex;flex-direction:column;align-items:center;justify-content:center;gap:8px;font-size:7.5px;font-weight:400}
.nav-cta svg{width:15px;height:15px}

.hero{position:absolute;top:64px;left:0;width:1200px;height:537px;background:linear-gradient(100deg,#e57877 0%,#ec8a86 40%,#f0a08e 70%,#e9837e 100%)}
.hotline{position:absolute;right:38px;top:22px;text-align:right;color:var(--white)}
.hotline b{font-weight:700;font-size:11px;display:block}
.hotline span{font-size:11.5px;display:block;margin-top:4px}
.hotline strong{font-size:19px;font-weight:400;display:block;margin-top:2px}
.hero-tabs{position:absolute;left:378px;top:101px;display:flex}
.hero-tabs a{width:148px;height:40px;display:flex;align-items:center;justify-content:center;font-size:8.5px;font-weight:400;background:var(--navy);color:var(--white)}
.hero-tabs a.active{background:var(--white);color:var(--red)}
.hero-card{position:absolute;left:350px;top:141px;width:500px;height:290px;background:rgba(255,235,235,.85);padding:36px 28px 0}
.hero-card h1{color:var(--red);font-weight:400;font-size:18.5px;line-height:19px}
.hero-card p{font-size:8.3px;line-height:15px;color:var(--muted);margin-top:16px}
.btn{display:flex;align-items:center;justify-content:center;background:var(--red);color:var(--white);font-size:11px;font-weight:400;height:40px}
.hero-card .btn{margin-top:30px;width:444px}

.intro{position:absolute;top:660px;left:0;width:1200px;text-align:center}
.intro h2{color:var(--red);font-weight:400;font-size:18.5px;line-height:23px}
.intro p{font-size:8.4px;line-height:15px;color:var(--muted);width:660px;margin:16px auto 0}
.intro p.note{font-weight:700;color:var(--text);margin-top:14px}

.benefits{position:absolute;top:866px;left:0;width:1200px;height:396px;background:linear-gradient(180deg,#0d2a6e,#0a2366 60%,#0e2a74);color:var(--white);text-align:center}
.benefits h2{font-weight:400;font-size:19px;margin-top:44px}
.benefits h2 b{font-weight:700}
.benefit-list{display:flex;justify-content:space-between;width:1125px;margin:34px auto 0;padding:0 12px}
.benefit{width:150px;font-size:10.5px;line-height:15px;font-weight:400}
.benefit i{display:block;width:62px;height:62px;border-radius:50%;background:var(--white);margin:0 auto 10px}
.benefits .btn{width:252px;margin:62px auto 0}

.faq{position:absolute;top:1305px;left:0;width:1200px}
.faq h2{text-align:center;color:var(--red);font-weight:400;font-size:19px}
.faq-box{position:absolute;top:54px;left:37px;width:1126px;height:252px;border:1px solid #ddd}
.faq-list{position:absolute;left:-1px;top:-1px;width:500px}
.faq-list a{display:flex;align-items:center;height:63px;padding-left:30px;background:var(--navy);color:var(--white);font-size:10px;font-weight:400;border-bottom:1px solid #10388f}
.faq-list a.active{background:var(--red);position:relative;width:509px;clip-path:polygon(0 0,500px 0,509px 50%,500px 100%,0 100%)}
.faq-answer{position:absolute;left:536px;top:36px;width:540px;font-size:8.4px;line-height:15px;color:var(--muted)}
.faq-answer ul{list-style:none;margin:15px 0 15px 10px}

.tips{position:absolute;top:1690px;left:0;width:1200px;height:615px;background:linear-gradient(90deg,#1f2e93 0%,#5a2478 40%,#c0154a 70%,#d2163e 100%)}
.tips h2{text-align:center;color:var(--white);font-weight:400;font-size:19px;margin-top:80px}
.tip-list{display:flex;gap:32px;justify-content:center;margin-top:28px}
.tip{width:208px;height:294px;background:var(--white);padding:32px 20px 0}
.tip h3{color:var(--red);font-weight:400;font-size:10.5px;line-height:15px}
.tip p{font-size:8.4px;line-height:15px;color:var(--muted);margin-top:15px}
.tips .btn{width:252px;margin:38px auto 0}

.help{position:absolute;top:2358px;left:0;width:1200px;text-align:center}
.help h2{color:var(--red);font-weight:700;font-size:23px}
.help p{font-size:11.5px;margin-top:2px;color:var(--text)}
.help strong{display:block;font-weight:400;font-size:19px;margin-top:2px}

.site-footer{position:absolute;top:2481px;left:0;width:1200px;height:40px;background:var(--footer);font-size:8.5px;color:var(--text);display:flex;align-items:center;justify-content:space-between;padding:0 38px}
.site-footer b{font-weight:700}
.site-footer nav{display:flex;gap:12px}
</style>
</head>
<body>

<header class="site-header">
  <a class="brand" href="#"><span class="brand-dot"></span>Visa Korvenet</a>
  <nav class="main-nav">
    <a href="#"><svg viewBox="0 0 16 16"><path d="M15 1 1 7l5 2 2 5 2-4-3-2 6-5-5 6 3 2z"/></svg>TOURISTEN VISUM</a>
    <a href="#"><svg viewBox="0 0 16 16"><path d="M5 3V2h6v1h4v11H1V3zm1 0h4V2.8H6z"/></svg>BUSINESS VISUM</a>
    <a href="#"><svg viewBox="0 0 16 16"><circle cx="8" cy="8" r="7.5"/><text x="8" y="12" text-anchor="middle" font-size="11" font-weight="700" fill="#022a7c" font-family="Montserrat,sans-serif">?</text></svg>WAS IST ETA?</a>
    <a href="#"><svg viewBox="0 0 16 16"><circle cx="8" cy="8" r="7.5"/><text x="8" y="11.5" text-anchor="middle" font-size="9" font-weight="700" fill="#022a7c" font-family="Montserrat,sans-serif">$</text></svg>AGB</a>
    <a href="#"><svg viewBox="0 0 16 16"><path d="M1 3h14v2L8 9 1 5zm0 3.5 7 4 7-4V13H1z"/></svg>KONTAKT</a>
  </nav>
  <a class="nav-cta" href="#"><svg viewBox="0 0 16 16"><rect x="1" y="1" width="14" height="14" rx="2" fill="#fff"/><path d="M4 12l1-3 5-5 2 2-5 5z" fill="#c8103a"/></svg>JETZT EVISITOR VISUM REGISTRIEREN</a>
</header>

<section class="hero" role="img" aria-label="Foto der Skyline von Sydney mit Opernhaus am Hafen, rötlich eingefärbt">
  <div class="hotline"><b>Sie brauchen Hilfe?</b><span>Kostenfreie Service Hotline von Mo-Fr 10-16 Uhr</span><strong>0800 5550147</strong></div>
  <div class="hero-tabs">
    <a class="active" href="#">EVISITOR VISUM AUSTRALIEN</a>
    <a href="#">EVISITOR TOURSIT ETA</a>
    <a href="#">EVISITOR BUSINISS ETA</a>
  </div>
  <div class="hero-card">
    <h1>Evisitor Visum Australien (Bis 2008 ETA - Electronic Travel Authority Australia)</h1>
    <p>Touristen und Geschäftsleute benötigen zur Einreise nach Australien vor Reisebeginn ein gültiges Visum, kurz „eVisitor“ Bis 2008 hieß dieses Visum noch (Electronic Travel Authority).<br>Eine Evisitor Registrierung ist wie ein Visum zeitlich begrenzt. Sowohl Touristen wie auch Geschäftsreisende können sich mit einem gültigen Evisitor Visum 3 Monate in Australien aufhalten. Evisitor Visa haben eine Gültigkeit von 12 Monaten, somit können Reisende innerhalb eines Jahres auch mehrfach nach Australien einreisen.</p>
    <a class="btn" href="#">JETZT EVISITOR VISUM REGISTRIEREN</a>
  </div>
</section>

<section class="intro">
  <h2>Visa-korvenet.org ist ein nicht staatlicher Servicedienstleister für die<br>Beantragung von Evisitor-Genehmigungen.</h2>
  <p>Bei uns erhalten Sie die Evisitor-Einreisegenehmigung einschließlich unserer Serviceleistung. Jeder Antrag wird von einem deutschsprachigen Support Mitarbeiter geprüft und bearbeitet. Damit Sie ohne Probleme, z.B. Formfehler, nach Australien einreisen können.</p>
  <p class="note">Sofern Sie den Antrag über uns anfordern, ist dieser 12 Monate ab Ausstellung gültig, es sein denn Ihr Reisepass läuft vorher ab.</p>
</section>

<section class="benefits" role="img" aria-label="Nächtliches Foto der Harbour Bridge in Sydney, dunkelblau eingefärbt">
  <h2>Ihre Vorteile mit <b>Visa</b> Korvenet</h2>
  <div class="benefit-list">
    <div class="benefit"><i></i>Anmeldeformular<br>auf deutsch</div>
    <div class="benefit"><i></i>Hilfe bei der<br>Formulareingabe</div>
    <div class="benefit"><i></i>Email Support</div>
    <div class="benefit"><i></i>Kontrolle Ihrer<br>gemachten Eingaben</div>
    <div class="benefit"><i></i>Statusnachricht<br>Ihres ETA-Antrages</div>
    <div class="benefit"><i></i>Aufbewahrung Ihrer<br>ETA Nummer für ein Jahr</div>
  </div>
  <a class="btn" href="#">JETZT EVISITOR VISUM REGISTRIEREN</a>
</section>

<section class="faq">
  <h2>Fragen &amp; Antworten</h2>
  <div class="faq-box">
    <div class="faq-list">
      <a class="active" href="#">Welche Dokumente erhalte ich mit meinem Evisitor Visum?</a>
      <a href="#">Wann erhalte ich meine Evisitor ETA VISA Genehmigung?</a>
      <a href="#">Was darf man als eVisitor (Inhaber eines ETA Visum) in Australien machen?</a>
      <a href="#">Welche Staaten können Evisitor für Australien in Anspruch nehmen?</a>
    </div>
    <div class="faq-answer">
      <p>Sobald Ihre Evisitor Genehmigung erteilt worden ist erhalten Sie eine Bestätigung per Email. Dieses Dokument müssen Sie aufheben und mit Ihren Reisedokumenten zur Reise mitnehmen. Die Evisitor Dokumente umfassen</p>
      <ul>
        <li>Ihre eVisitor Genehmigungsnummer</li>
        <li>Das Datum ab dem Ihre eVisitor Nummer gültig ist</li>
        <li>Die allgemeinen eVisitor Konditionen und Bedingungen</li>
      </ul>
      <p>Mit einer gültigen eVisitornummer (ETA Visum) erhalten Sie bei der Einreise nach Australien keinen Eintrag, bzw. Stempel mehr in Ihren Reisepass. Die Crew Ihrer Airline übermittelt bereits während des Fluges Ihre Pass und eVisitor Daten an die Australischen Behörden.</p>
    </div>
  </div>
</section>

<section class="tips" role="img" aria-label="Foto einer Surferin mit Brett am Strand, blau-rot eingefärbt">
  <h2>3 Tipps für eine erfolgreiche Australien Reise</h2>
  <div class="tip-list">
    <article class="tip">
      <h3>Gültige Reisedokumente für die gesamte Dauer des Aufenthaltes.</h3>
      <p>Reisepass und vorläufiger Reisepass werden anerkannt. Kinder benötigen einen eigenen Reisepass. Personalausweis und vorläufiger Personalausweis sind nicht zugelassen Sollten asiatische Staaten im Zuge der Reise besucht werden wollen, informieren Sie sich bitte über die speziellen Vorschriften, da manche Staaten eine Gültigkeit bis zu sechs Monaten ausländischer Reisepässe voraussetzen.</p>
    </article>
    <article class="tip">
      <h3>Anweisungen folge leisten und somit Ärger vermeiden.</h3>
      <p>Australien hat sehr strikte Einreise und Quarantänevorschriften. An etlichen Flughäfen ist mit Körperscannern bei der Einreise zu rechnen. Ebenso müssen eingeführte Nahrungsmittel, Tier- und Pflanzenprodukte auf der Einreisekarte angegeben werden. Striktes Befolgen der Anweisungen wird von uns empfohlen um unnötige Wartezeiten und Ärger zu vermeiden.</p>
    </article>
    <article class="tip">
      <h3>Halten Sie sich an die Gesetze des Landes.</h3>
      <p>Wie bereits erwähnt ist Australien ein liberales Land, solange die Gesetze befolgt werden. Illegale Aktivitäten wie Verstöße gegen die Visa Bestimmungen, die Ausfuhr von kulturellen Schätzen oder die Einnahme von illegalen Substanzen können zur Ausweisung bis hin zu Freiheitsstrafe in Australien führen.</p>
    </article>
  </div>
  <a class="btn" href="#">JETZT EVISITOR VISUM REGISTRIEREN</a>
</section>

<section class="help">
  <h2>Sie brauchen Hilfe?</h2>
  <p>Kostenfreie Service Hotline von Mo-Fr 10-16 Uhr</p>
  <strong>0800 5550147</strong>
</section>

<footer class="site-footer">
  <span><b>VISA</b>-Korvenet.org © 2017</span>
  <nav><a href="#">Datenschutz</a><a href="#">AGB</a><a href="#">Impressum</a></nav>
</footer>

</body>
</html>
```